Landing Page Design for Adult Dating Age Verification (18+)

The objective of this task is to design a visually appealing pre-landing page for the adult dating site "Plumvelle (site: https://plumvelle.example/)" with an age verification mechanism. The pre-landing page will feature two buttons that redirect visitors to the main offer. The design should also include a footer block that includes links to the terms of use, privacy policy, and contact us pages.

Design Requirements:
Develop an age verification section prominently displayed on the pre-landing page.
Design the section to include two buttons labeled "Yes" and "No" for visitors to confirm their age.
Ensure the section is visually appealing and clearly communicates the purpose of age verification.

Visual Appeal:
Create a visually appealing design that aligns with the branding and theme of the "Plumvelle" adult dating site.
Use suitable color schemes, typography, and graphics to enhance the overall visual appeal of the pre-landing page.

Layout and Navigation:
Design an engaging and intuitive layout that encourages visitors to interact with the page and proceed to the main offer.
Ensure clear and visible navigation elements that direct visitors to the main offer or provide additional information.

Responsive Design:
Develop a responsive design that provides a seamless user experience across various devices, including desktop and mobile.
Ensure the design elements and layout adapt well to different screen sizes and resolutions.

File Formats and Assets:
Deliver the final design in PSD, AI, or Sketch format, ensuring that the files are well-organized and layered.
Include any necessary images or assets used in the design, ensuring they are of high quality and optimized for web use.

```html
<!DOCTYPE html>
<html lang="en">
<head>
<meta charset="utf-8">
<title>Plumvelle — Age Verification</title>
<link rel="stylesheet" href="https://fonts.googleapis.com/css2?family=Barlow:wght@400;500;600;700&family=Playfair+Display:wght@700&display=swap">
<style>
  :root {
    --lavender: #dcc3e6;
    --lavender-soft: rgba(196, 150, 196, 0.5);
    --white: #ffffff;
    --green: #7bbf45;
    --red: #d72b2b;
    --ink: #2f2f2f;
    --footer-bg: #ffffff;
  }
  * { box-sizing: border-box; margin: 0; padding: 0; }
  html, body { width: 1200px; height: 761px; overflow: hidden; }
  body { font-family: "Barlow", sans-serif; background: var(--footer-bg); position: relative; }

  .hero {
    position: absolute; left: 0; top: 0; width: 1200px; height: 686px;
    background:
      radial-gradient(ellipse at 50% 45%, #c9a89a 0%, rgba(150,110,100,0.6) 35%, transparent 65%),
      linear-gradient(100deg, #b9aea6 0%, #8f7d74 30%, #7d6258 55%, #6e5049 75%, #4a3a3a 100%);
  }
  .hero__shade {
    position: absolute; inset: 0;
    background: linear-gradient(180deg, rgba(0,0,0,0) 55%, rgba(40,25,30,0.45) 100%);
  }

  .brand {
    position: absolute; left: 111px; top: 34px;
    display: flex; align-items: center; gap: 12px;
  }
  .brand__dot { width: 52px; height: 52px; border-radius: 50%; background: var(--lavender); }
  .brand__name {
    font-family: "Playfair Display", serif; font-weight: 700;
    font-size: 30px; color: var(--white); letter-spacing: 0.5px;
  }

  .sign-in {
    position: absolute; left: 1026px; top: 66px;
    display: flex; align-items: center; gap: 7px;
    color: var(--white); font-weight: 600; font-size: 15px; text-decoration: none;
  }

  .age-gate {
    position: absolute; left: 269px; top: 219px; width: 663px; height: 247px;
    border: 4px solid var(--lavender); border-radius: 12px;
    background: var(--lavender-soft);
    text-align: center; color: var(--white);
  }
  .age-gate__title {
    font-family: "Playfair Display", serif; font-weight: 700;
    font-size: 26px; margin-top: 55px; letter-spacing: 0.3px;
  }
  .age-gate__text { font-size: 14px; margin-top: 12px; }
  .age-gate__actions { display: flex; justify-content: center; gap: 23px; margin-top: 20px; }
  .btn {
    width: 175px; height: 42px; border-radius: 21px;
    display: flex; align-items: center; justify-content: center;
    color: var(--white); font-weight: 700; font-size: 15px; text-decoration: none;
  }
  .btn--confirm { background: var(--green); }
  .btn--exit { background: var(--red); }

  .footer {
    position: absolute; left: 0; top: 686px; width: 1200px; height: 75px;
    display: flex; align-items: center; color: var(--ink); font-size: 14.5px;
  }
  .footer__links { position: absolute; left: 111px; display: flex; gap: 20px; }
  .footer__links a { color: var(--ink); text-decoration: none; }
  .footer__copy { position: absolute; right: 111px; }
  .footer__code { position: absolute; left: 1134px; font-size: 11px; }
</style>
</head>
<body>
  <section class="hero">
    <div class="hero__photo" role="img" aria-label="Romantic photograph of a couple embracing on a bed in a loft bedroom" style="position:absolute;inset:0;"></div>
    <div class="hero__shade"></div>

    <a class="brand" href="https://plumvelle.example/">
      <span class="brand__dot"></span>
      <span class="brand__name">Plumvelle</span>
    </a>

    <a class="sign-in" href="https://plumvelle.example/">
      <svg width="13" height="14" viewBox="0 0 13 14" aria-hidden="true">
        <circle cx="6.5" cy="4" r="3.5" fill="#fff"/>
        <path d="M0 14 C0 9 3 8 6.5 8 C10 8 13 9 13 14 Z" fill="#fff"/>
      </svg>
      Sign in
    </a>

    <div class="age-gate">
      <h1 class="age-gate__title">ADULT CONTENT - ACCESS RESTRICTED</h1>
      <p class="age-gate__text">Please confirm that you’re over 18 or leave the website</p>
      <div class="age-gate__actions">
        <a class="btn btn--confirm" href="https://plumvelle.example/">I’m Over 18</a>
        <a class="btn btn--exit" href="#">Exit</a>
      </div>
    </div>
  </section>

  <footer class="footer">
    <nav class="footer__links">
      <a href="#">Terms of use</a><span>|</span>
      <a href="#">Privacy policy</a><span>|</span>
      <a href="#">Contact us</a>
    </nav>
    <span class="footer__copy">© Copyrights 2023 | All Rights Reserved</span>
    <span class="footer__code">C38</span>
  </footer>
</body>
</html>
```